New Flyer Design Project Brenwick Doors and Interiors

Real photos will be added but please start with these for layout. Copy will be supplied so you can just leave a text box to start I am open to suggestions. Thank you

Target Market(s)

Builders, Designers, remodelers, consumers

Colors

Designer to choose colors to be used in the design.

Requirements
Must have
• Before and after photos, email, phone, logo, description

```html
<!DOCTYPE html>
<html lang="en">
<head>
<meta charset="utf-8">
<title>Brenwick Doors and Interiors – Flyer</title>
<link rel="stylesheet" href="https://fonts.googleapis.com/css2?family=Oswald:wght@300&family=Source+Sans+3:wght@400;600&display=swap">
<style>
  :root{
    --teal:#5fa8a2;
    --teal-light:#67aaa5;
    --charcoal:#545456;
    --rule-green:#6f8e76;
    --ink:#4a4a4c;
    --paper:#ffffff;
    --frame:#c9c9c9;
  }
  *{margin:0;padding:0;box-sizing:border-box}
  html,body{width:976px;height:1200px;overflow:hidden;background:var(--paper)}
  .flyer{position:relative;width:976px;height:1200px;overflow:hidden;background:var(--paper);font-family:"Source Sans 3",sans-serif;color:var(--ink)}
  .brand-name{position:absolute;left:44px;top:46px;font-size:62px;font-weight:600;color:var(--teal);letter-spacing:.5px}
  .header-rule{position:absolute;left:0;top:139px;width:494px;height:4px;background:var(--rule-green)}
  .title-panel{position:absolute;left:0;top:143px;width:494px;height:410px;background:var(--charcoal)}
  .headline{position:absolute;left:38px;top:168px;width:540px;font-family:"Oswald",sans-serif;font-weight:300;font-size:58px;line-height:74px;color:var(--teal-light);text-transform:uppercase;letter-spacing:-.5px;white-space:nowrap;transform:scaleX(.84);transform-origin:left top}
  .service-list{position:absolute;left:44px;top:346px;list-style:none;color:#fff;font-size:28px;line-height:33px}
  .tagline-bar{position:absolute;left:0;top:501px;width:440px;height:52px;background:var(--teal);color:#fff;font-size:27px;line-height:52px;padding-left:39px}
  .hero-photo{position:absolute;left:494px;top:29px;width:469px;height:544px;border:3px solid var(--frame)}
  .side-accent{position:absolute;left:963px;top:143px;width:13px;height:392px;background:var(--charcoal)}
  .gallery-photo{position:absolute;width:216px;height:216px;border:2px solid var(--frame)}
  .description{position:absolute;left:518px;top:627px;width:433px;font-size:19px;line-height:23.7px;text-align:justify;hyphens:auto}
  .description p+p{margin-top:23.7px}
  .footer-rule{position:absolute;left:0;top:1096px;width:976px;height:6px;background:var(--charcoal)}
  .contact-bar{position:absolute;left:0;top:1102px;width:976px;height:98px;background:var(--teal);color:#fff;font-size:25px}
  .contact-item{position:absolute;top:0;height:98px;display:flex;align-items:center;gap:8px}
  .contact-item svg{flex:none}
  .contact-email{left:38px}
  .contact-web{left:438px}
  .contact-phone{right:22px;gap:18px}
</style>
</head>
<body>
<main class="flyer">
  <div class="brand-name">Brenwick</div>
  <div class="header-rule"></div>

  <section class="title-panel"></section>
  <h1 class="headline">Vintage Doors and<br>Interior Restoration</h1>
  <ul class="service-list">
    <li>VINTAGE DECOR</li>
    <li>IRON ARTS</li>
    <li>ANTIQUE DOORS</li>
    <li>INTERIOR DECOR</li>
  </ul>
  <div class="tagline-bar">HOME INPROVEMENT</div>

  <div class="hero-photo" role="img" aria-label="Weathered pale blue antique double door with iron grilles, a crystal chandelier, gilt armchair and flowers" style="background:linear-gradient(90deg,#8a6e4e 0%,#b9a68a 25%,#c9d2cd 45%,#c2ccc8 70%,#8f7658 100%)"></div>
  <div class="side-accent"></div>

  <div class="gallery-photo" role="img" aria-label="Rustic wooden door with black wrought iron scroll hardware" style="left:39px;top:619px;background:linear-gradient(135deg,#7b634a,#4d3d2e)"></div>
  <div class="gallery-photo" role="img" aria-label="Open antique glass doors leading to a bright living room" style="left:279px;top:619px;background:linear-gradient(135deg,#a89a86,#d8d2c6)"></div>
  <div class="gallery-photo" role="img" aria-label="Bedroom with canopy bed and ornate iron bed frame" style="left:39px;top:852px;background:linear-gradient(135deg,#c9b48f,#6b4a3a)"></div>
  <div class="gallery-photo" role="img" aria-label="Close-up of a black iron bar across a white distressed door" style="left:279px;top:852px;background:linear-gradient(135deg,#d8d6d0,#8d8b86)"></div>

  <article class="description">
    <p>When walking up to any home or building the first place you generally go is to the front door. It’s the welcoming point, the place where first impressions are made. You can dramatically change the appearances of any building with just a little work and some imagination.</p>
    <p>Doors have changed throughout the years along with the varied styles of architecture. Whether its interior doors, exterior doors, we have them all. Our selection of Oak, Pine, Chestnut, Mahogany, and Iron is among the largest and most diversified collection available on-line. Changing a door in your home isn’t a big deal.</p>
    <p>Change is good…don’t be afraid of a little work. Hard work pays off and in the end will be very rewarding.</p>
  </article>

  <div class="footer-rule"></div>
  <footer class="contact-bar">
    <div class="contact-item contact-email">
      <svg width="20" height="18" viewBox="0 0 20 18" fill="none" stroke="#fff" stroke-width="1.8"><path d="M2 7 L10 2 L18 7 V16 H2 Z"/><path d="M2 7 L10 12 L18 7"/></svg>
      <span>hello@brenwickdoors.com</span>
    </div>
    <div class="contact-item contact-web">
      <svg width="20" height="20" viewBox="0 0 20 20" fill="none" stroke="#fff" stroke-width="1.5"><circle cx="10" cy="10" r="8.5"/><ellipse cx="10" cy="10" rx="4" ry="8.5"/><path d="M1.5 10H18.5M3 5.5H17M3 14.5H17"/></svg>
      <span>www.brenwickdoors.com</span>
    </div>
    <div class="contact-item contact-phone">
      <svg width="26" height="20" viewBox="0 0 26 20" fill="#fff"><path d="M1 6 C1 2 25 2 25 6 V8 H19 V5.5 H7 V8 H1 Z"/><path d="M5 9 H21 L23 19 H3 Z"/><circle cx="13" cy="13.5" r="3" fill="#5fa8a2"/></svg>
      <span>555 014 2287</span>
    </div>
  </footer>
</main>
</body>
</html>
```